Seminar Flyer

We would like a flyer describing a seminar we will be presenting to window cleaners. The seminar topic is Glass Restoration and will include discussions on types of glass, types of glass damage and solutions. I am including the following (sample) description:
"Spend a day with The PaneSage and learn how you can benefit from learning "Glass Restoration" and the many benefits to offering this service to your clients.
Before investing a lot of "time and money" in ANY Glass Restoration System, learn what Glass Restoration is all about and how you can turn a small investment into a very profitable business. And, this new business can be easily expanded into several other related business's.
Ready to expand your business and make some great money?
"DON'T WAIT" - Start offering your clients Glass Restoration Services.
"Glass Restoration" is one of the most profitable "Add-On" businesses for the window cleaning industry and you now have an opportunity to learn from one of the industry
leaders. Roy Hatcher will be offering a full day "hands-on" seminar on Glass Restoration.
The seminar will cover:
Glass Types
Glass Damage
Glass Coatings
Glass Distortion & Breakage
Glass Restoration Systems
Glass Restoration Procedures
Customer Expectations
Marketing and Pricing a job
Hands on demonstrations
And much much more.....
And did I mention it will cover "Glass"?
This full day seminar will be presented by Roy Hatcher and sponsored by the B.Mollendorf Company at their facility in Carson, California.
Space will be limited, so you must register to attend, but the seminar and lunch is FREE.
This all day seminar will also cover discussions on:
Hard Water Spot Removal and methods for removing.
What exactly is "Tin Etch Haze" and how to prevent or remove it easily.
Minor scratch removal (light scratches and metal marks)
Tempered Glass Defects - Waivers and precautions
Excess Scratch removal (tempered Glass scratching)
Graffiti Removal (major scratch and acid etch damage)
Additional Money Makers:
Anti-Graffiti Film Application
- An easy add on business for glass restoration businesses
Hard Water Spot Removal and Glass Sealant
- An easy add on business for window cleaning businesses
Window Frame Restoration and Treatment
- An easy add on business for window cleaning businesses"
Roy Hatcher, the President of The Hatcher Company, is well known in the window cleaning industry as "PaneSage", so we want to make sure that branding is included in the flyer.
PLEASE NOTE: The flyer will be distributed as an e-mail attachment so the flyer itself will not have any specific information regarding dates and location.
Target Market(s)
Window Cleaners; small business owners.
Industry/Entity Type
Window Cleaning
Look and feel

```html
<!DOCTYPE html>
<html lang="en">
<head>
<meta charset="utf-8">
<title>Glass Restoration Seminar</title>
<link rel="stylesheet" href="https://fonts.googleapis.com/css2?family=Alegreya+Sans+SC:wght@700;800;900&family=Baloo+2:wght@800&family=Open+Sans:wght@700&display=swap">
<style>
  :root {
    --page: #ffffff;
    --band: #c4b59a;
    --sheet: #bdbec1;
    --ink: #5a4a3e;
    --ink-dark: #3b322c;
    --orange: #f7931e;
    --outline: #5b4a3c;
    --photo-a: #6d7478;
    --photo-b: #9a9c98;
    --photo-c: #8e8f8c;
  }
  * { margin: 0; padding: 0; box-sizing: border-box; }
  html, body { width: 1200px; height: 900px; overflow: hidden; background: var(--page); }
  .flyer {
    position: absolute; left: 271px; top: 0; width: 667px; height: 900px;
    background: var(--sheet); overflow: hidden;
    font-family: "Alegreya Sans SC", sans-serif; color: var(--ink);
  }
  .masthead { position: absolute; left: 0; top: 0; width: 667px; height: 193px; background: var(--band); }
  .title {
    position: absolute; left: 66px;
    font-family: "Baloo 2", sans-serif; font-weight: 800; font-size: 60px; line-height: 1;
    color: var(--orange); -webkit-text-stroke: 2px var(--outline);
    text-shadow: 3px 3px 0 var(--outline); letter-spacing: -1px;
  }
  .title-top { top: 22px; }
  .title-bottom { top: 88px; }
  .presenter {
    position: absolute; left: 330px; top: 88px; width: 260px; text-align: center;
    transform: rotate(-10deg); transform-origin: center;
    font-family: "Baloo 2", sans-serif; font-weight: 800; color: var(--orange);
    -webkit-text-stroke: 1px var(--outline); text-shadow: 2px 2px 0 var(--outline); line-height: 1;
  }
  .presenter .by { font-size: 14px; display: block; }
  .presenter .nick { font-size: 28px; display: block; }
  .presenter .name { font-size: 28px; display: block; }
  .intro, .pitch {
    position: absolute; font-weight: 800; font-size: 18px; line-height: 26.5px;
  }
  .intro { left: 57px; top: 192px; width: 580px; }
  .pitch { left: 47px; top: 415px; width: 590px; line-height: 25.5px; }
  .callout {
    position: absolute; left: 0; top: 278px; width: 667px; text-align: center;
    font-weight: 800; font-size: 27px; line-height: 35.5px;
    color: var(--orange); -webkit-text-stroke: 1px var(--outline);
  }
  .topics {
    position: absolute; left: 45px; top: 565px; list-style: none;
    font-weight: 800; font-size: 17px; line-height: 22px;
  }
  .caption {
    position: absolute; font-family: "Open Sans", sans-serif; font-weight: 700; font-size: 14px;
    color: var(--ink-dark); text-align: center; white-space: nowrap; transform: translateX(-50%);
  }
  .photo { position: absolute; }
  .photo-acid { left: 339px; top: 593px; width: 119px; height: 89px; background: linear-gradient(135deg, var(--photo-a), var(--photo-b)); }
  .photo-during { left: 498px; top: 593px; width: 119px; height: 89px; background: linear-gradient(135deg, var(--photo-c), var(--photo-a)); }
  .photo-after { left: 395px; top: 715px; width: 157px; height: 117px; background: linear-gradient(135deg, var(--photo-b), var(--photo-a)); }
  .footer {
    position: absolute; left: 0; top: 840px; width: 667px; text-align: center;
    font-weight: 900; font-size: 20px; line-height: 25px; color: var(--ink-dark);
  }
</style>
</head>
<body>
<main class="flyer">
  <header class="masthead">
    <h1 class="title title-top">GLASS RESTORATION</h1>
    <div class="title title-bottom">SEMINAR</div>
    <div class="presenter">
      <span class="by">BY</span>
      <span class="nick">“ PANESAGE ”</span>
      <span class="name">ROY HATCHER</span>
    </div>
  </header>

  <p class="intro">Spend a day with The PaneSage and learn how you can benefit from learning "Glass Restoration" and the many benefits to offering this service to your clients.</p>

  <p class="callout">Ready to expand your business<br>and make some great money?<br>"DON'T WAIT" - Start offering your clients<br>Glass Restoration Services</p>

  <p class="pitch">Glass Restoration" is one of the most profitable "Add-On" businesses for the window cleaning industry and you now have an opportunity to learn from one of the industry leaders. Roy Hatcher will be offering a full day "hands-on" seminar on Glass Restoration.</p>

  <ul class="topics">
    <li>The seminar will cover:</li>
    <li>Glass Types</li>
    <li>Glass Damage</li>
    <li>Glass Coatings</li>
    <li>Glass Distortion &amp; Breakage</li>
    <li>Glass Restoration Systems</li>
    <li>Glass Restoration Procedures</li>
    <li>Customer Expectations</li>
    <li>Marketing and Pricing a job</li>
    <li>Hands on demonstrations</li>
    <li>And much much more.....</li>
    <li>And did I mention it will cover "Glass"?</li>
  </ul>

  <span class="caption" style="left:398px; top:571px;">ACID DAMAGE</span>
  <div class="photo photo-acid" role="img" aria-label="Storefront window with acid etch graffiti damage"></div>
  <span class="caption" style="left:557px; top:571px;">DURING RESTORATION</span>
  <div class="photo photo-during" role="img" aria-label="Storefront window partway through glass restoration"></div>
  <span class="caption" style="left:474px; top:692px;">AFTER RESTORATION</span>
  <div class="photo photo-after" role="img" aria-label="Storefront window with clear glass after restoration"></div>

  <p class="footer">Space will be limited, so you must register to attend<br>SEMINAR and LUNCH is FREE.</p>
</main>
</body>
</html>
```